I need a feather flag designed for my business which states " HELICOPTER RIDES" and possibly adding my logo to them. This will be used for my helicopter ride business and we can put these up to show people where the rides will be .

Industry/Entity Type

aviation

Colors
00AB8E
00BBA5
67D7C9
C6EFE9
E9F9F6
EB3D1F
EC4F4E
F09395
F8D3D4
FCEDEE

Requirements
Must have
• logo

```html
<!DOCTYPE html>
<html lang="en">
<head>
<meta charset="utf-8">
<title>Helicopter Rides Feather Flag</title>
<link rel="stylesheet" href="https://fonts.googleapis.com/css2?family=Barlow+Condensed:ital,wght@0,400;1,500&display=swap">
<style>
  :root {
    --backdrop: #b3b3b3;
    --flag-navy: #121826;
    --flag-edge: #0a0d16;
    --accent-red: #d10a0a;
    --accent-white: #eeeeee;
    --text-white: #f4f4f4;
  }
  html, body {
    margin: 0;
    padding: 0;
    width: 1200px;
    height: 1001px;
    overflow: hidden;
    background: var(--backdrop);
  }
  .flag-canvas {
    display: block;
    width: 1200px;
    height: 1001px;
  }
  .flag-body { fill: var(--flag-navy); }
  .flag-sleeve { fill: var(--flag-edge); }
  .stripe-red { fill: var(--accent-red); }
  .stripe-white { fill: var(--accent-white); }
  .logo-text {
    font-family: "Barlow Condensed", sans-serif;
    font-weight: 400;
    font-size: 46px;
    fill: var(--text-white);
  }
  .headline {
    font-family: "Barlow Condensed", sans-serif;
    font-style: italic;
    font-weight: 500;
    font-size: 142px;
  }
  .headline-main { fill: var(--text-white); }
  .headline-accent { fill: var(--accent-red); }
</style>
</head>
<body>
<svg class="flag-canvas" viewBox="0 0 1500 1251" xmlns="http://www.w3.org/2000/svg" aria-label="Two Helicopter Rides feather flags">
  <defs>
    <g id="feather-flag">
      <path class="flag-body" d="M365 950 L365 330 C365 220 460 140 590 138 L590 950 Z"/>
      <path class="flag-sleeve" d="M365 950 L365 330 C365 300 370 280 376 262 L376 950 Z"/>
      <path class="stripe-red" d="M386 265 C390 255 394 248 399 242 L405 480 L400 480 Z"/>
      <path class="stripe-white" d="M372 950 L398 950 L404 608 Z"/>
      <path class="stripe-white" d="M556 142 L578 138 L548 470 Z"/>
      <path class="stripe-red" d="M548 610 L578 950 L560 950 Z"/>
      <text class="logo-text" x="475" y="305" text-anchor="middle">COMPANY</text>
      <text class="logo-text" x="475" y="345" text-anchor="middle">LOGO</text>
      <text class="headline" transform="translate(524 925) rotate(-90)" textLength="530" lengthAdjust="spacingAndGlyphs"><tspan class="headline-main">HELICOPTER </tspan><tspan class="headline-accent">RIDES</tspan></text>
    </g>
  </defs>
  <use href="#feather-flag"/>
  <use href="#feather-flag" x="550"/>
</svg>
</body>
</html>
```